Business Card design for Property Developer

We need a business card design for a Melbourne based Property Developer called "Kestrelmoor Holdings Pty Ltd".

We subdivide land and onsell to builders etc.

We already have a company logo, which is attached. Also I have attached the layout requirements from the printer. We would like a 2-sided design with one side displaying our logo by itself and the other with the required info, such as name, address, tel no., email, abn etc. The card will need to be used by 4 members of staff so name and contact details should be interchangable.
Updates

If possible, can you please write "name' "job position" "phone" "email" "address" on the card but leave them so I can add the details at a later time. Thank you. Also I plan on printing with UV spot printing as a background on the card. Keep this is mind when designing.

Thanks again.

Hello designers, please do not include pics of houses, house plansĀ or construction machinery etc as we really do not like the way it looks. Thank you.

Target Market(s)

Real Estate Agents, Land Owners, Local Council Departments, Govt Bodies, other Developers etc.

Industry/Entity Type

Business

Requirements
Must have
• 2-sided design with one side displaying our logo by itself and the other with the required info, such as name, address, tel no., email, abn etc.

```html
<!DOCTYPE html>
<html lang="en">
<head>
<meta charset="utf-8">
<title>Kestrelmoor Holdings – Business Card</title>
<link rel="stylesheet" href="https://fonts.googleapis.com/css2?family=Arimo:wght@400;700&display=swap">
<style>
  :root {
    --card-bg: #ffffff;
    --stripe-blue: #0079c1;
    --accent-blue: #0a8fd6;
    --label-blue: #1aa0e0;
    --brand-navy: #263c8c;
    --ink: #000000;
  }
  html, body {
    margin: 0;
    padding: 0;
    width: 1200px;
    height: 783px;
    overflow: hidden;
    background: var(--card-bg);
  }
  .card {
    display: block;
    width: 1200px;
    height: 783px;
    background: var(--card-bg);
    font-family: "Arimo", Arial, sans-serif;
  }
  .stripe { fill: var(--stripe-blue); }
  .brand-dot { fill: var(--brand-navy); }
  .brand-name { fill: var(--brand-navy); font-size: 27px; font-weight: 700; }
  .person-name { fill: var(--accent-blue); font-size: 32px; font-weight: 700; }
  .job-position { fill: var(--ink); font-size: 27px; }
  .contact-line { fill: var(--ink); font-size: 27px; }
  .contact-label { fill: var(--label-blue); }
</style>
</head>
<body>
<svg class="card" viewBox="0 0 1076 709" preserveAspectRatio="none" xmlns="http://www.w3.org/2000/svg">
  <g class="brand">
    <circle class="brand-dot" cx="406" cy="199" r="14"/>
    <text class="brand-name" x="430" y="209">Kestrelmoor Holdings</text>
  </g>

  <g class="stripes">
    <polygon class="stripe" points="785,273 800,299 76,709 30,709"/>
    <polygon class="stripe" points="757,341 772,366 165,709 118,709"/>
  </g>

  <g class="identity">
    <text class="person-name" transform="translate(164,606) rotate(-28.5)">PERSON NAME</text>
    <text class="job-position" transform="translate(403,472) rotate(-28.5)">Job Position</text>
  </g>

  <g class="contact">
    <text class="contact-line" transform="translate(553,544) rotate(-28.5)"><tspan class="contact-label">Phone</tspan> 000-000-0000</text>
    <text class="contact-line" transform="translate(571,576) rotate(-28.5)"><tspan class="contact-label">Email</tspan> asdf@KestrelmoorHoldings.com</text>
    <text class="contact-line" transform="translate(591,609) rotate(-28.5)">Suite 000, Street Name</text>
    <text class="contact-line" transform="translate(611,641) rotate(-28.5)">City, Province, Pin-Code</text>
  </g>
</svg>
</body>
</html>
```